Website Redesign for an Appointment Setting and Lead Generation Company.

I need to redesign an existing website. The website that we are looking to be redesigned is www.trellisvane.example. TrellisVane is a B2B appointment setting organization. The idea is to present a modern look website for professional services company. The idea is to engage the user, look at various services and generate more inbound leads for the website

Target Market(s)

US, APAC, Europe, UK. Focused on B2B companies more than $100 Mn

Industry/Entity Type

Professional Service

Number of Pages Required

5+ page

Font styles to use
Other font styles liked:
• Roboto

Requirements
Must have
• Home Page - Banner Image, Section for Client testimonials
Industry Page - To show industry capabilities
Services Page - To show service capabilities
Blogs Page - to show blogs
Offerings Page - Offerings Page
Nice to have
• I would like to have a elegant design with small animation. Preferably use colors from the logo attached. Use infographics where possible

```html
<!DOCTYPE html>
<html lang="en">
<head>
<meta charset="utf-8">
<title>TrellisVane – B2B Lead Generation</title>
<link href="https://fonts.googleapis.com/css2?family=Roboto:wght@300;400;500;700&display=swap" rel="stylesheet">
<style>
:root{
  --red:#cc3238;
  --red-soft:#dd6468;
  --ink:#222;
  --body:#444;
  --muted:#666;
  --grey-panel:#e4e4e4;
  --card-label:#6b6b6b;
  --white:#fff;
}
*{box-sizing:border-box;margin:0;padding:0}
html,body{width:1200px;height:2340px;overflow:hidden;background:var(--white)}
body{font-family:'Roboto',sans-serif;color:var(--body)}
.page{position:relative;width:1200px;height:2340px}
.abs{position:absolute}

/* header */
.brand{left:150px;top:14px;display:flex;align-items:center;gap:8px}
.brand-dot{width:22px;height:22px;border-radius:50%;background:var(--red)}
.brand-name{font-size:24px;font-weight:500;color:var(--red)}
.nav{left:382px;top:22px;display:flex;gap:40px;font-size:11px;color:#333}
.nav span.drop::after{content:"";display:inline-block;width:4px;height:4px;border-right:1px solid #333;border-bottom:1px solid #333;transform:rotate(45deg);margin-left:5px;position:relative;top:-2px}
.search{left:929px;top:23px}
.btn-contact{left:957px;top:17px;width:94px;height:26px;border-radius:5px;background:var(--red);color:#fff;font-size:11px;font-weight:700;display:flex;align-items:center;justify-content:center}

/* hero */
.hero{left:150px;top:60px;width:901px;height:337px;background:linear-gradient(100deg,#2b2b2b 0%,#3a3a3a 50%,#4a4a4a 80%,#8a8a8a 100%)}
.hero-title{left:199px;top:125px;font-size:39px;line-height:45px;font-weight:700;color:#fff;letter-spacing:-.3px}
.hero-text{left:201px;top:227px;width:400px;font-size:11px;line-height:13.5px;color:#fff}
.btn-more{left:201px;top:287px;width:120px;height:37px;border-radius:5px;background:var(--red);color:#fff;font-size:12px;font-weight:500;display:flex;align-items:center;justify-content:center}

/* section bands */
.band{left:150px;background:linear-gradient(90deg,var(--red),var(--red-soft));color:#fff;border-radius:0 24px 24px 0;font-weight:500;font-size:16px;line-height:19px;display:flex;align-items:center;padding-left:50px}

.intro{left:176px;top:496px;width:850px;font-size:12.5px;line-height:20.3px;font-weight:300;text-align:center;color:#333}
.intro strong{font-weight:500;color:#222}

/* cards */
.card{top:634px;width:225px;height:210px}
.card-media{width:225px;height:178px}
.card-label{height:32px;background:var(--card-label);color:#fff;font-size:11.5px;display:flex;align-items:center;justify-content:center}
.card-label.active{background:linear-gradient(90deg,var(--red),var(--red-soft));font-size:13px;font-weight:500}
.card-media.text{background:#3a3d44;color:#fff;font-size:8.5px;line-height:16.3px;text-align:center;padding:30px 14px 0;text-transform:uppercase}

/* stats */
.stats-bg{left:150px;top:973px;width:900px;height:412px;background:linear-gradient(180deg,#5b6470 0%,#7a8592 45%,#4c535d 100%)}
.stat{width:191px;height:155px;border-radius:50%;background:#fff;border:6px solid var(--red);box-shadow:0 0 0 3px rgba(204,50,56,.35);display:flex;flex-direction:column;align-items:center;justify-content:center;text-align:center;color:var(--red)}
.stat b{font-size:37px;font-weight:700;line-height:42px}
.stat span{font-size:14px;line-height:17px;margin-top:4px}

/* testimonial */
.quote{left:315px;top:1492px;width:572px;height:116px;border:2px solid var(--red);font-size:12px;line-height:22.5px;font-weight:300;text-align:center;color:#333;padding:10px 50px 0}
.attribution{left:150px;top:1629px;width:901px;text-align:center;font-size:12px;font-weight:500;color:#222}
.dots{left:570px;top:1656px;display:flex;gap:7px;align-items:center}
.dots i{display:block;width:7px;height:7px;border-radius:50%;background:var(--red)}
.dots i.on{width:30px;border-radius:4px}

/* contact */
.contact{left:150px;top:1685px;width:901px;height:300px;background:var(--grey-panel)}
.field{height:33px;background:#fff;border-radius:2px;font-size:10px;color:#666;padding:11px 14px}
.field em{color:var(--red);font-style:normal}
.consent{left:609px;top:1811px;width:382px;font-size:8.6px;line-height:11.5px;color:#333}
.consent .check{display:flex;align-items:center;gap:8px;font-size:10px;font-weight:500;color:#222;margin-bottom:9px}
.consent .box{width:14px;height:14px;border:1.5px solid #333;background:#fff}
.consent p{margin-bottom:11px}
.consent a{color:#2a4fa8;text-decoration:underline}
.btn-submit{left:763px;top:1919px;width:90px;height:26px;background:var(--red);border-radius:3px;color:#fff;font-size:10px;font-weight:700;display:flex;align-items:center;justify-content:center}

/* footer */
.fcol h4{font-size:16px;font-weight:500;color:#333;margin-bottom:20px}
.fcol li{list-style:none;font-size:11px;color:#666;height:27.7px}
.socials{left:854px;top:2184px;display:flex;gap:14px}
.socials i{display:block;width:28px;height:28px;border-radius:50%;border:3px solid var(--red)}
.fbrand{left:856px;top:2236px;display:flex;align-items:center;gap:6px}
.fbrand .brand-dot{width:20px;height:20px}
.fbrand .brand-name{font-size:21px}
.bottom-bar{left:150px;top:2286px;width:901px;height:37px;background:linear-gradient(90deg,var(--red),var(--red-soft));color:#fff;font-size:9px;display:flex;align-items:center;justify-content:center;gap:5px}
.bottom-bar b{font-weight:700}
</style>
</head>
<body>
<div class="page">

  <header>
    <div class="abs brand"><span class="brand-dot"></span><span class="brand-name">TrellisVane</span></div>
    <nav class="abs nav"><span>Home</span><span class="drop">About</span><span class="drop">Services</span><span class="drop">Our Expertise</span><span class="drop">Library</span></nav>
    <svg class="abs search" width="12" height="12" viewBox="0 0 12 12"><circle cx="5" cy="5" r="3.8" fill="none" stroke="#cc3238" stroke-width="1.2"/><line x1="7.8" y1="7.8" x2="11" y2="11" stroke="#cc3238" stroke-width="1.3"/></svg>
    <div class="abs btn-contact">Contact Us</div>
  </header>

  <section>
    <div class="abs hero" role="img" aria-label="Dark desk with notebook, pen, smartphone and laptop keyboard"></div>
    <h1 class="abs hero-title">Build Your Sales Pipeline<br>in the New Normal</h1>
    <p class="abs hero-text">Providing end-to-end webinar management services - including platform support, audience acquisition, providing subject matter expert speakers, webinar moderation, reporting, and lead nurturing on the webinar attendees</p>
    <div class="abs btn-more">Know More</div>
  </section>

  <section>
    <h2 class="abs band" style="top:416px;width:525px;height:53px">Offering Dynamic Solutions for your Niche Product Offerings</h2>
    <p class="abs intro">We are a leading B2B lead generation company with presence across North America, Europe, APAC and India. Our experienced and trained lead generation executives understand your unique service offerings and work along your campaign journey to achieve the desired goals. Leveraging our extensive proprietary database, we target key decision-makers &amp; influencers across industries. Our sales lead generation services are custom-made for your service offerings, be it next-generation technologies like machine learning, digital transformation, analytics, and artificial intelligence. We work as an extension of your team and deliver results that matter to your business – <strong>Improve Sales Pipeline and Acquire New Customers.</strong></p>

    <div class="abs card" style="left:195px">
      <div class="card-media" style="background:radial-gradient(circle at 55% 45%,#5a8fb0 0%,#3d5a6b 30%,#2a1e16 65%)" role="img" aria-label="Desk globe in a warmly lit room"></div>
      <div class="card-label">GLOBAL PARTNER</div>
    </div>
    <div class="abs card" style="left:488px">
      <div class="card-media text">15,000+ campaigns executed across 12 verticals and 100+ service lines for offerings across business process management, technology services, machine learning, robotic process management, artificial intelligence and many more</div>
      <div class="card-label active">DOMAIN EXPERTISE</div>
    </div>
    <div class="abs card" style="left:780px">
      <div class="card-media" style="background:linear-gradient(135deg,#e9edf2,#c9d6e4 50%,#f3f4f6)" role="img" aria-label="Blue interlocking gears with business icons"></div>
      <div class="card-label">PROPRIETRY SYSTEMS</div>
    </div>
  </section>

  <section>
    <div class="abs stats-bg" role="img" aria-label="Skyscrapers seen from below with an airplane in the sky"></div>
    <h2 class="abs band" style="top:904px;width:525px;height:69px">Let your Sales Team focus on Closures with our B2B Lead<br>Generation Services</h2>
    <div class="abs stat" style="left:212px;top:1003px"><b>3800</b><span>Research Reports<br>Generated</span></div>
    <div class="abs stat" style="left:505px;top:1003px"><b>80%</b><span>Client Retention<br>Rate</span></div>
    <div class="abs stat" style="left:797px;top:1003px"><b>500+</b><span>Surveys and Interviews<br>conducted per month</span></div>
    <div class="abs stat" style="left:212px;top:1198px"><b>50%</b><span>Leads Generated<br>with CXOs &amp; VPs</span></div>
    <div class="abs stat" style="left:505px;top:1198px"><b>33</b><span>Events<br>Managed</span></div>
    <div class="abs stat" style="left:797px;top:1198px"><b>20</b><span>Databases<br>Subscribed</span></div>
  </section>

  <section>
    <h2 class="abs band" style="top:1408px;width:248px;height:52px">What Our Clients Say...</h2>
    <blockquote class="abs quote">Trellis Vane has been an important partnet in our marketing value chain. The Highly energitic team form TVI has always accpeted our targets as its own. Their innovative approach and dedication to our requirements makes us reach out to them frequently.</blockquote>
    <p class="abs attribution">Chief Marketing officer- Global technology consulting and digital solutions Company</p>
    <div class="abs dots"><i class="on"></i><i></i><i></i></div>
  </section>

  <section>
    <div class="abs contact"></div>
    <h2 class="abs band" style="top:1685px;width:165px;height:52px;padding-left:42px">Contact Us</h2>
    <div class="abs field" style="left:217px;top:1761px;width:188px">Name<em>*</em></div>
    <div class="abs field" style="left:413px;top:1761px;width:187px">Email<em>*</em></div>
    <div class="abs field" style="left:607px;top:1761px;width:188px">Phone number<em>*</em></div>
    <div class="abs field" style="left:803px;top:1761px;width:187px">Company name<em>*</em></div>
    <div class="abs field" style="left:217px;top:1803px;width:383px;height:150px">Message</div>
    <div class="abs consent">
      <div class="check"><span class="box"></span>I agree to receive other communications from TrellisVane.</div>
      <p>You can unsubscribe from these communications at any time. For more information on how to unsubscribe, our privacy practices, and how we are committed to protecting and respecting your privacy, please review our <a>Privacy Policy</a>.</p>
      <p>By clicking submit below, you consent to allow TrellisVane to store and process the personal information submitted above to provide you the content requested.</p>
    </div>
    <div class="abs btn-submit">Submit</div>
  </section>

  <footer>
    <div class="abs fcol" style="left:283px;top:2013px"><h4>ABOUT US</h4><ul><li>About</li><li>Our Team</li><li>Awards</li><li>Our Partnerships</li><li>Our Differentiators</li><li>Locations</li></ul></div>
    <div class="abs fcol" style="left:570px;top:2013px"><h4>SERVICES</h4><ul><li>B2B Appointment Setting</li><li>Account Based Marketing</li><li>Research As A Service</li><li>Event Audience Acquisition</li><li>Staffing &amp; Talent Acquisition</li><li>Digital Marketing</li><li>Social Media Research</li><li>Lead Nurturing</li></ul></div>
    <div class="abs fcol" style="left:854px;top:2013px"><h4>LIBRARY</h4><ul><li>Videos</li><li>Infographics</li><li>Blog</li><li>Case Studies</li></ul></div>
    <div class="abs socials" aria-label="Social links"><i></i><i></i><i></i></div>
    <div class="abs fbrand"><span class="brand-dot"></span><span class="brand-name">TrellisVane</span></div>
    <div class="abs bottom-bar"><b>Privacy Policy</b><span>|</span><span>Copyright All Rights Reserved © 2020</span></div>
  </footer>

</div>
</body>
</html>
```